Flyer for Custom Home Builder!

my company is Harlow Ridge Homes, I am looking for a flyer that we can send via email to a customer, or print and hand out. I am thinking four pages so we could print this and fold it., possibly creating a folder. The name of the company is Harlow Ridge Homes our website is here www.harlowridgehomes-example.com. Some text you can use "Crafting luxury homes isn't just a job, it's our passion.
With meticulous attention to detail and an unwavering commitment to using the finest materials, Harlow Ridge Homes consistently delivers exceptional results that stand as a testament to our commitment to quality."

"Trust is the cornerstone of our foundation.
With a proven track record of delivering on our promises for over 16 years, we prioritize transparent communication and integrity throughout every step of the home-building journey".

you may need to obtain the photos here
https://files.example-share.net/f/k27pw4m8zrt03xq61bnv/h?key=48vn2c9q1x7mb5t0ekd3h&dl=0

Target Market(s)

We build homes for every wealthy clients, therefore the photos are extremely important

Industry/Entity Type

Construction.

Requirements
Must have
• clear larger photos

```html
<!DOCTYPE html>
<html lang="en">
<head>
<meta charset="utf-8">
<title>Harlow Ridge Homes – Flyer</title>
<link rel="stylesheet" href="https://fonts.googleapis.com/css2?family=Montserrat:wght@300;400;700;800&display=swap">
<style>
  :root {
    --page-bg: #f7f7f7;
    --orange: #f4a553;
    --orange-light: #f7b56c;
    --orange-deep: #ee9a45;
    --navy: #0a2a7c;
    --navy-mid: #123c9c;
    --navy-light: #1d55b8;
    --white: #ffffff;
    --accent: #f5a24e;
  }
  * { box-sizing: border-box; margin: 0; padding: 0; }
  html, body { width: 849px; height: 1200px; overflow: hidden; background: var(--page-bg); }
  body { font-family: 'Montserrat', sans-serif; color: var(--white); }

  .flyer { position: relative; width: 849px; height: 1200px; }

  .backdrop { position: absolute; left: 24px; top: 24px; width: 801px; height: 1153px; }

  .brand {
    position: absolute; top: 96px; left: 0; width: 849px; text-align: center;
    font-weight: 800; font-size: 28px; letter-spacing: 3px; line-height: 1;
  }

  .headline {
    position: absolute; top: 184px; left: 0; width: 849px; text-align: center;
  }
  .headline__main { font-weight: 700; font-size: 35px; line-height: 40px; letter-spacing: -0.3px; }
  .headline__sub { font-weight: 300; font-size: 35px; line-height: 44px; margin-top: 4px; }

  .intro {
    position: absolute; top: 287px; left: 62px; width: 725px; text-align: center;
    font-weight: 300; font-size: 16px; line-height: 23.5px;
  }

  .hero-photo { position: absolute; left: 55px; top: 385px; width: 738px; height: 492px; display: block; }

  .trust {
    position: absolute; top: 906px; left: 50px; width: 749px; text-align: center;
    font-size: 16px; line-height: 23.5px; font-weight: 300;
  }
  .trust__lead { font-weight: 700; font-size: 15.5px; }

  .contact { position: absolute; top: 1022px; left: 0; width: 849px; text-align: center; }
  .contact__phone { font-weight: 700; font-size: 54px; line-height: 62px; color: var(--accent); letter-spacing: -1px; }
  .contact__address { font-weight: 400; font-size: 19px; line-height: 24px; margin-top: 9px; letter-spacing: 0.3px; }
  .contact__web { font-weight: 400; font-size: 15.5px; line-height: 20px; margin-top: 6px; letter-spacing: 0.4px; }
</style>
</head>
<body>
<main class="flyer">
  <svg class="backdrop" viewBox="0 0 801 1153" aria-hidden="true">
    <defs>
      <linearGradient id="warm" x1="0" y1="0" x2="0" y2="1">
        <stop offset="0" stop-color="var(--orange-light)"/>
        <stop offset="1" stop-color="var(--orange-deep)"/>
      </linearGradient>
      <linearGradient id="deep" x1="0" y1="0" x2="1" y2="1">
        <stop offset="0" stop-color="var(--navy-light)"/>
        <stop offset="0.5" stop-color="var(--navy-mid)"/>
        <stop offset="1" stop-color="var(--navy)"/>
      </linearGradient>
    </defs>
    <rect x="0" y="0" width="801" height="1153" fill="url(#warm)"/>
    <polygon points="0,869 801,337 801,1133 0,1133" fill="url(#deep)"/>
    <rect x="0" y="1133" width="801" height="20" fill="var(--orange)"/>
  </svg>

  <div class="brand">HARLOW RIDGE HOMES</div>

  <h1 class="headline">
    <div class="headline__main">CRAFTING LUXURY HOMES</div>
    <div class="headline__sub">isn't just a job, it's our passion.</div>
  </h1>

  <p class="intro">With meticulous attention to detail and an unwavering commitment to using the finest materials, Harlow Ridge Homes consistently delivers exceptional results that stand as a testament to our commitment to quality</p>

  <svg class="hero-photo" viewBox="0 0 738 492" role="img" aria-label="Photo of a modern luxury home with an infinity pool, spa and covered outdoor lounge under a blue sky">
    <defs>
      <linearGradient id="scene" x1="0" y1="0" x2="0" y2="1">
        <stop offset="0" stop-color="#9cc6ee"/>
        <stop offset="0.45" stop-color="#d9d6cf"/>
        <stop offset="0.7" stop-color="#7fc6cf"/>
        <stop offset="1" stop-color="#a7a29b"/>
      </linearGradient>
    </defs>
    <rect width="738" height="492" fill="url(#scene)"/>
  </svg>

  <section class="trust">
    <p class="trust__lead">Trust is the cornerstone of our foundation.</p>
    <p>With a proven track record of delivering on our promises for over 16 years, we prioritize transparent communication and integrity throughout every step of the home-building journey</p>
  </section>

  <section class="contact">
    <div class="contact__phone">512-555-0187</div>
    <div class="contact__address">4870 CEDAR BLUFF LANE, SUITE 200, AUSTIN TX 78701</div>
    <div class="contact__web">www.harlowridgehomes-example.com</div>
  </section>
</main>
</body>
</html>
```